Pecan Ridge Paving. Chip Seal Done Right

I need my card to have all my basic information on it. Keep it simple. Include web site, phone number and email address. Include phrase Chip Seal Done Right or Pecan Ridge’s Top Paving Company. Keep card simple. Include color and logo. Put all contact info on card. Make card simple and not complicated.

Here is infuriation yo out in business card

Dale R. Whitmore
830.555.0173 cell phone
Dalewhitmore7@mailbarn.net
www.pecanridgepaving.net

Target Market(s)

Hill Country Texas USA

Industry/Entity Type

Road chip seal

Contact Information for Business Card

We chip seal roads for ranches and property owners

Font styles to use
Serif
Sans Serif
Decorative
Script

Colors
0054AA
0677BA
7BADD7
CADEEF
E8F1F8
EB3D1F
EC4F4E
F09395
F8D3D4
FCEDEE

Requirements
Must have
• Keep it simply
Nice to have
• Logo and all basic info

```html
<!DOCTYPE html>
<html lang="en">
<head>
<meta charset="utf-8">
<title>Pecan Ridge Paving – Business Card</title>
<link rel="stylesheet" href="https://fonts.googleapis.com/css2?family=Nunito+Sans:wght@400;600;800&display=swap">
<style>
  :root {
    --navy: #1c2550;
    --red: #ae2333;
    --white: #ffffff;
    --backdrop: #ecebe8;
    --ink: #1c2550;
  }
  * { margin: 0; padding: 0; box-sizing: border-box; }
  html, body { width: 1200px; height: 999px; overflow: hidden; }
  body {
    background: var(--backdrop);
    font-family: "Nunito Sans", Arial, sans-serif;
    position: relative;
  }
  .card {
    position: absolute;
    left: 213px; top: 278px;
    width: 775px; height: 442px;
    background: var(--white);
    box-shadow: 0 6px 18px rgba(0,0,0,0.18);
    overflow: hidden;
  }
  .brand {
    position: absolute;
    left: 38px; top: 132px;
    display: flex; align-items: center; gap: 18px;
  }
  .brand-dot {
    width: 74px; height: 74px; border-radius: 50%;
    background: var(--red);
    flex: none;
  }
  .brand-name {
    color: var(--navy);
    font-weight: 800;
    font-size: 31px;
    line-height: 1.12;
    letter-spacing: 0.5px;
    text-transform: uppercase;
  }
  .divider {
    position: absolute;
    left: 437px; top: 70px;
    width: 3px; height: 270px;
    background: var(--red);
  }
  .contact-name {
    position: absolute;
    left: 479px; top: 183px;
    color: var(--ink);
    font-size: 17px;
    font-weight: 800;
    line-height: 22px;
  }
  .contacts {
    position: absolute;
    left: 479px; top: 217px;
    list-style: none;
    color: var(--ink);
    font-size: 15px;
    line-height: 20px;
  }
  .contacts li { display: flex; align-items: flex-start; gap: 10px; }
  .contacts li + li { margin-top: 5px; }
  .contacts .phone { margin-top: 10px; }
  .contacts .email { margin-top: 9px; }
  .contacts svg { width: 20px; height: 20px; flex: none; }
  .tagline-band {
    position: absolute;
    left: 0; bottom: 0;
    width: 435px; height: 52px;
    background: var(--navy);
    color: var(--white);
    font-size: 23px;
    font-weight: 600;
    line-height: 52px;
    padding-left: 50px;
    letter-spacing: 0.3px;
  }
  .accent-band {
    position: absolute;
    left: 442px; bottom: 0;
    width: 333px; height: 21px;
    background: var(--red);
  }
</style>
</head>
<body>
  <div class="card">
    <div class="brand">
      <span class="brand-dot"></span>
      <div class="brand-name">Pecan Ridge<br>Paving</div>
    </div>

    <div class="divider"></div>

    <p class="contact-name">Dale R. Whitmore</p>

    <ul class="contacts">
      <li>
        <svg viewBox="0 0 20 20" aria-hidden="true"><circle cx="10" cy="10" r="10" fill="var(--red)"/><circle cx="10" cy="10" r="5.5" fill="none" stroke="#fff" stroke-width="1.4"/><path d="M4.5 10h11M10 4.5c2.5 3 2.5 8 0 11M10 4.5c-2.5 3-2.5 8 0 11" fill="none" stroke="#fff" stroke-width="1.1"/></svg>
        <span>www.pecanridgepaving.net</span>
      </li>
      <li>
        <svg viewBox="0 0 20 20" aria-hidden="true"><circle cx="10" cy="10" r="10" fill="var(--red)"/><path d="M10 4.5a4 4 0 0 1 4 4c0 3-4 7-4 7s-4-4-4-7a4 4 0 0 1 4-4z" fill="#fff"/><circle cx="10" cy="8.5" r="1.6" fill="var(--red)"/></svg>
        <span>418 Mesquite Ln,<br>Fredonia, TX 76842</span>
      </li>
      <li class="phone">
        <svg viewBox="0 0 20 20" aria-hidden="true"><circle cx="10" cy="10" r="10" fill="var(--red)"/><path d="M6.5 5.2l2 .2.9 2.3-1.2.9c.6 1.3 1.6 2.3 2.9 2.9l.9-1.2 2.3.9.2 2c-.3.6-1 1-1.7 1-4 0-7.3-3.3-7.3-7.3 0-.7.4-1.4 1-1.7z" fill="#fff"/></svg>
        <span>830.555.0173</span>
      </li>
      <li class="email">
        <svg viewBox="0 0 20 20" aria-hidden="true"><circle cx="10" cy="10" r="10" fill="var(--red)"/><rect x="5" y="6.5" width="10" height="7" rx="1" fill="none" stroke="#fff" stroke-width="1.3"/><path d="M5.3 7l4.7 3.6L14.7 7" fill="none" stroke="#fff" stroke-width="1.3"/></svg>
        <span>Dalewhitmore7@mailbarn.net</span>
      </li>
    </ul>

    <div class="tagline-band">CHIP SEAL DONE RIGHT</div>
    <div class="accent-band"></div>
  </div>
</body>
</html>
```